Verostel business card

Business card for sustainable investment company called "Verostel". Verostel is an exchange platform selling carbon credits between buyers and sellers. Carbon Credits are an environmental commodity for reducing global carbon emissions.

the card should obviously have our logo and the theme should be sustainability/environment mixed with a trading platform.

Contact Information for Business Card

Logo, Name, Title, Phone, Email

Colors
0054AA
0677BA
7BADD7
CADEEF
E8F1F8
0094D4
00A9DD
6FCCEA
C7EBF8
E9F6FB
00AB8E
00BBA5
67D7C9
C6EFE9
E9F9F6
59FF00
82FF00
B8FF75
E3FFCB
F4FFEA

```html
<!DOCTYPE html>
<html lang="en">
<head>
<meta charset="UTF-8">
<title>Verostel Business Card</title>
<link href="https://fonts.googleapis.com/css2?family=Poppins:wght@400;500;600&display=swap" rel="stylesheet">
<style>
  :root {
    --page-bg: #e4e4e4;
    --card-bg: #ffffff;
    --ink-navy: #1f2b45;
    --brand-blue: #1f7ae6;
    --brand-cyan: #2fd6ec;
    --text-dark: #1c1c1c;
  }
  html, body {
    margin: 0;
    padding: 0;
    width: 1200px;
    height: 900px;
    overflow: hidden;
    background: var(--page-bg);
    font-family: "Poppins", sans-serif;
  }
  .canvas {
    position: relative;
    width: 1200px;
    height: 900px;
  }
  .card {
    position: absolute;
    top: 217px;
    width: 308px;
    height: 499px;
    background: var(--card-bg);
  }
  .card-front {
    left: 279px;
    border-radius: 0 69px 0 69px;
  }
  .card-back {
    left: 617px;
    border-radius: 69px 0 69px 0;
  }
  .front-wordmark {
    position: absolute;
    left: 0;
    right: 0;
    top: 228px;
    text-align: center;
    font-weight: 600;
    font-size: 40px;
    letter-spacing: 1px;
    color: var(--brand-blue);
  }
  .back-brand {
    position: absolute;
    left: 24px;
    top: 166px;
    display: flex;
    align-items: center;
    gap: 16px;
  }
  .brand-dot {
    width: 40px;
    height: 40px;
    border-radius: 50%;
    background: var(--brand-blue);
  }
  .brand-name {
    font-weight: 600;
    font-size: 34px;
    line-height: 1;
    color: var(--ink-navy);
    letter-spacing: 0.5px;
  }
  .person {
    position: absolute;
    left: 32px;
    top: 316px;
  }
  .person-name {
    margin: 0;
    font-weight: 600;
    font-size: 20px;
    line-height: 1.1;
    color: var(--ink-navy);
    letter-spacing: 0.3px;
  }
  .person-title {
    margin: 0;
    font-weight: 400;
    font-size: 15px;
    line-height: 1.2;
    color: var(--brand-blue);
  }
  .contact-list {
    list-style: none;
    margin: 0;
    padding: 0;
    position: absolute;
    left: 32px;
    top: 370px;
  }
  .contact-item {
    display: flex;
    align-items: center;
    gap: 5px;
    height: 18px;
    font-size: 14.5px;
    color: var(--text-dark);
  }
  .contact-icon {
    width: 13px;
    height: 13px;
    flex: none;
  }
</style>
</head>
<body>
<main class="canvas">
  <section class="card card-front">
    <div class="front-wordmark">VEROSTEL</div>
  </section>

  <section class="card card-back">
    <div class="back-brand">
      <span class="brand-dot"></span>
      <span class="brand-name">VEROSTEL</span>
    </div>

    <div class="person">
      <p class="person-name">DANIEL HARTWELL</p>
      <p class="person-title">Managing Director</p>
    </div>

    <ul class="contact-list">
      <li class="contact-item">
        <svg class="contact-icon" viewBox="0 0 24 24" aria-hidden="true">
          <path d="M6.6 10.8a15.1 15.1 0 0 0 6.6 6.6l2.2-2.2c.3-.3.7-.4 1-.2 1.1.4 2.3.6 3.6.6.6 0 1 .4 1 1V20c0 .6-.4 1-1 1A17 17 0 0 1 3 4c0-.6.4-1 1-1h3.5c.6 0 1 .4 1 1 0 1.3.2 2.5.6 3.6.1.3 0 .7-.2 1z" fill="var(--brand-blue)"/>
        </svg>
        044-987 654 321
      </li>
      <li class="contact-item">
        <svg class="contact-icon" viewBox="0 0 24 24" aria-hidden="true">
          <rect x="2" y="5" width="20" height="14" fill="var(--brand-blue)"/>
          <path d="M2 5l10 8 10-8M2 19l7-7M22 19l-7-7" stroke="#fff" stroke-width="1.5" fill="none"/>
        </svg>
        info@verostelmail.com
      </li>
      <li class="contact-item">
        <svg class="contact-icon" viewBox="0 0 24 24" aria-hidden="true">
          <g fill="none" stroke="var(--brand-blue)" stroke-width="2">
            <circle cx="12" cy="12" r="10"/>
            <ellipse cx="12" cy="12" rx="4.5" ry="10"/>
            <path d="M2 12h20M4 7h16M4 17h16"/>
          </g>
        </svg>
        www.verostelsite.com
      </li>
    </ul>
  </section>
</main>
</body>
</html>
```